Create a wine label for our soon to be released Sparkling Wine

As we are about to release our new Sparkling Wine we are in need of a new label. Dimensions and text as per attached file, the design is more or less free style, but keep it a classic sparkling wine label. Keep it clean. Bottle will be near to black with black/silver cap You can use Script Font. No green, red or gold colours. We like black and silver, but don't be afraid to use some color somewhere (we can always change that). We thought of printing our logo in silver foil so a black label would be nice.

Target Market(s)

wine industry

Font styles to use
Script
Other font styles liked:
• GaramITC

Requirements
Must have
• Dimensions and text as per attached file
Nice to have
• Classic wine label
Should not have
• No gold or red or green colour

```html
<!DOCTYPE html>
<html lang="en">
<head>
<meta charset="utf-8">
<title>Frost Hollow Vintage Sparkling Label</title>
<link rel="stylesheet" href="https://fonts.googleapis.com/css2?family=Great+Vibes&family=Yesteryear&display=swap">
<style>
  :root {
    --label-black: #000000;
    --ink-white: #ffffff;
    --silver-light: #f2f2f2;
    --silver-mid: #b9b9b9;
    --silver-dark: #7d7d7d;
    --vignette-light: #ffffff;
    --vignette-shade: #e4e4e4;
  }
  html, body {
    margin: 0;
    padding: 0;
    overflow: hidden;
    background: var(--label-black);
  }
  .label {
    position: relative;
    width: 1200px;
    height: 1200px;
    background: var(--label-black);
    color: var(--ink-white);
    overflow: hidden;
  }
  .label > * {
    position: absolute;
    left: 0;
    width: 100%;
    margin: 0;
    text-align: center;
    line-height: 1;
    font-weight: 400;
  }
  .winery-name {
    top: 52px;
    left: 20px;
    font-family: "Great Vibes", cursive;
    font-size: 150px;
  }
  .region {
    top: 240px;
    left: -18px;
    font-family: "Yesteryear", cursive;
    font-size: 62px;
  }
  .crest {
    top: 326px;
    left: 352px;
    width: 496px;
    height: 302px;
  }
  .vintage-year {
    top: 662px;
    left: -10px;
    font-family: "Yesteryear", cursive;
    font-size: 96px;
  }
  .wine-style {
    top: 752px;
    left: 10px;
    font-family: "Great Vibes", cursive;
    font-size: 150px;
  }
  .wine-details {
    top: 1018px;
    left: 0;
    font-family: "Yesteryear", cursive;
    font-size: 62px;
    line-height: 1.0;
  }
  .wine-details span { display: block; }
</style>
</head>
<body>
  <main class="label">
    <h1 class="winery-name">Frost Hollow</h1>
    <p class="region">Tasmania</p>

    <svg class="crest" viewBox="0 0 496 302" xmlns="http://www.w3.org/2000/svg">
      <defs>
        <linearGradient id="silver-frame" x1="0" y1="0" x2="0" y2="1">
          <stop offset="0" stop-color="var(--silver-dark)"/>
          <stop offset="0.3" stop-color="var(--silver-light)"/>
          <stop offset="0.55" stop-color="var(--silver-mid)"/>
          <stop offset="0.8" stop-color="var(--silver-light)"/>
          <stop offset="1" stop-color="var(--silver-dark)"/>
        </linearGradient>
        <radialGradient id="vignette-fill" cx="0.5" cy="0.5" r="0.6">
          <stop offset="0" stop-color="var(--vignette-light)"/>
          <stop offset="0.7" stop-color="#f6f6f6"/>
          <stop offset="1" stop-color="var(--vignette-shade)"/>
        </radialGradient>
      </defs>
      <ellipse class="crest-frame" cx="248" cy="151" rx="246" ry="149" fill="url(#silver-frame)"/>
      <ellipse class="crest-inner-edge" cx="248" cy="151" rx="232" ry="136" fill="var(--silver-dark)"/>
      <ellipse class="crest-vignette" cx="248" cy="151" rx="229" ry="133" fill="url(#vignette-fill)"
               role="img" aria-label="Ink illustration of a bare windswept tree beside mountain ridges with a winding silver stream"/>
    </svg>

    <p class="vintage-year">2013</p>
    <h2 class="wine-style">Vintage Sparkling</h2>
    <p class="wine-details">
      <span>Blanc de Noir</span>
      <span>Méthode Traditionnelle</span>
    </p>
  </main>
</body>
</html>
```